furnace plenum sticker

This sticker is left at every job above the furnace or on the duct work connected to the furnace.
It needs to be bold so that when homeowner is at the furnace during a break down they see it. Phone number and what we do needs to be prominate. It is our calling card for service.
Sticker needs to look corporate and professional.

New logo (attached) must be incorporated into sticker.

Current sticker attached
Size
8.5 inches x 5.5 inches

Target Market(s)

residential home owners

Industry/Entity Type

Work

Colors
ec1f27

Requirements
Must have
• Our new current logo attached

```html
<!DOCTYPE html>
<html lang="en">
<head>
<meta charset="utf-8">
<title>Northbay Heating and Air Conditioning – Service Sticker</title>
<link href="https://fonts.googleapis.com/css2?family=Roboto:wght@700;900&family=Stardos+Stencil:wght@700&display=swap" rel="stylesheet">
<style>
  :root {
    --brand-red: #ec1f27;
    --sticker-yellow: #ffea00;
    --ink: #050505;
    --ribbon-white: #f4f4f4;
    --ribbon-gold: #c9a912;
    --ribbon-gold-dark: #b39510;
    --backdrop: #ececec;
  }
  * { margin: 0; padding: 0; box-sizing: border-box; }
  html, body { width: 1200px; height: 799px; overflow: hidden; }
  body { background: var(--backdrop); position: relative; font-family: "Roboto", Arial, sans-serif; }

  .sticker {
    position: absolute; left: 148px; top: 64px; width: 905px; height: 586px;
    background: var(--ink);
  }
  .main-panel {
    position: absolute; left: 12px; top: 12px; width: 881px; height: 458px;
    background: var(--sticker-yellow); border-radius: 32px;
  }
  .ribbon { position: absolute; top: -12px; width: 130px; height: 196px; }
  .ribbon--flag { left: 36px; }
  .ribbon--member { left: 715px; }

  .brand {
    position: absolute; left: 0; right: 0; top: 52px; text-align: center;
  }
  .brand-name {
    color: var(--brand-red); font-weight: 900; font-size: 84px; line-height: 84px;
    letter-spacing: 1px;
  }
  .brand-tagline {
    color: var(--ink); font-weight: 700; font-size: 30px; line-height: 1;
    margin-top: -4px; letter-spacing: 0.3px;
  }
  .service-band {
    position: absolute; left: 36px; top: 222px; width: 809px; height: 143px;
    background: var(--ink);
  }
  .service-band svg { display: block; }
  .service-line {
    position: absolute; left: 0; right: 0; top: 394px; text-align: center;
    font-weight: 700; font-size: 30px; line-height: 1; color: var(--ink);
    white-space: nowrap;
  }

  .contact {
    position: absolute; top: 492px; width: 360px; text-align: center; color: var(--sticker-yellow);
    white-space: nowrap;
  }
  .contact--west { left: 31px; }
  .contact--east { left: 510px; }
  .contact-area { font-weight: 700; font-size: 23px; line-height: 1.1; letter-spacing: 0.5px; }
  .contact-phone { font-weight: 700; font-size: 50px; line-height: 1.05; letter-spacing: -0.5px; }
  .hours-icon { position: absolute; left: 407px; top: 483px; }
</style>
</head>
<body>
  <div class="sticker">
    <div class="main-panel">
      <svg class="ribbon ribbon--flag" viewBox="0 0 130 196" aria-hidden="true">
        <polygon points="0,0 130,0 130,196 65,140 0,196" fill="var(--ribbon-white)"/>
        <polygon points="0,0 24,0 24,176 0,196" fill="var(--brand-red)"/>
        <polygon points="106,0 130,0 130,196 106,176" fill="var(--brand-red)"/>
      </svg>
      <svg class="ribbon ribbon--member" viewBox="0 0 130 196" aria-hidden="true">
        <polygon points="0,0 130,0 130,196 65,140 0,196" fill="var(--ribbon-white)"/>
        <polygon points="0,0 24,0 24,176 0,196" fill="var(--ribbon-gold)"/>
        <polygon points="106,0 130,0 130,196 106,176" fill="var(--ribbon-gold-dark)"/>
      </svg>

      <div class="brand">
        <div class="brand-name">NORTHBAY</div>
        <div class="brand-tagline">HEATING AND AIR CONDITIONING</div>
      </div>

      <div class="service-band">
        <svg width="809" height="143" viewBox="0 0 809 143">
          <text x="404" y="128" text-anchor="middle" textLength="790" lengthAdjust="spacingAndGlyphs"
                font-family="'Stardos Stencil', Impact, sans-serif" font-weight="700" font-size="160"
                fill="var(--sticker-yellow)">SERVICED</text>
        </svg>
      </div>

      <p class="service-line">We service all makes and models. Repairs and installations.</p>
    </div>

    <div class="contact contact--west">
      <div class="contact-area">Burlington / Hamilton</div>
      <div class="contact-phone">905-555-0147</div>
    </div>

    <svg class="hours-icon" width="90" height="90" viewBox="0 0 90 90" aria-label="24 hour service">
      <circle cx="45" cy="45" r="44" fill="var(--sticker-yellow)"/>
      <path d="M45 13 A32 32 0 1 1 17 29" fill="none" stroke="var(--ink)" stroke-width="6"/>
      <polygon points="56,6 56,22 68,13" fill="var(--ink)" transform="translate(-12,1)"/>
      <text x="45" y="52" text-anchor="middle" font-family="Roboto, Arial, sans-serif" font-weight="900" font-size="20" fill="var(--ink)">24hr</text>
    </svg>

    <div class="contact contact--east">
      <div class="contact-area">Oakville / Milton</div>
      <div class="contact-phone">905-555-0183</div>
    </div>
  </div>
</body>
</html>
```